Banner Ad Design Project

I need a banner design. The website is under construction at www.brightmarrow.example

Name: Bright Marrow
Tagline: Steady Sparks for crowded calendars

This is a leadership development and executive coaching site. The past site is live at www.quillstepnow.example. (so you can get a sense of the content)

The audience are (BUSY) executives, senior managers, leaders and top professionals, so the feel needs to be highly professional but also modern and fresh. I want to communicate energy but also solid and trust worthy and not too new agey. The audience are also people with strong social values who want to change things - so not too corporate (Ie suits!)

I would like the design to be floating on a white background, very clean and simple. I am attracted to reds or sunset (burn orange crimson colors.) But totally open to any color ideas.
I am giving an open brief for your ideas.
Here are the dimensions 960px wide, roughly 190px height.

Reason: The weekend might give more time to designers to get involved. Thanks Vina

Hi designers

You may not have seen the additions I gave to this brief.

The banner should not have leader out front photo's. Maybe less corporate than I initially thought. 
Not too corporate (no suits!) Please no chess pieces, jigsaw pieces, cartoon images, cliche leadership images. 
Am am trying for inspiration /inspiring whilst still being professional. Very simple and clean.
Please can the design be floating in a white background so that the web page is borderless - A bit like it is in http://palmoriskel.example/
Thank you

Target Market(s)

Senior managers, executives but people who also want to change the world!

Industry/Entity Type

Construction

Requirements
Should not have
• Should not have leader out front photo's.
Maybe less corporate than I initially thought.
Am am trying for inspiration /inspiring whilst still being professional.
Please no chess pieces, jigsaw pieces, cartoon images, cliche leadership images. Not too corporate (Ie suits!)

Thanks

```html
<!DOCTYPE html>
<html lang="en">
<head>
<meta charset="utf-8">
<title>Bright Marrow — Steady Sparks for crowded calendars</title>
<link rel="stylesheet" href="https://fonts.googleapis.com/css2?family=Fira+Sans:wght@400&display=swap">
<style>
  :root {
    --paper: #ffffff;
    --ink: #1f1d1e;
    --tagline-grey: #8a8a8a;
    --blossom-light: #fbe9d9;
    --blossom-mid: #f3cfb0;
  }
  html, body {
    margin: 0;
    padding: 0;
    overflow: hidden;
    background: var(--paper);
  }
  .banner {
    position: relative;
    width: 1200px;
    height: 238px;
    background: var(--paper);
    overflow: hidden;
    font-family: "Fira Sans", sans-serif;
  }
  .brand-name {
    position: absolute;
    left: 54px;
    top: 32px;
    margin: 0;
    font-size: 104px;
    font-weight: 400;
    line-height: 1;
    letter-spacing: -0.5px;
    color: var(--ink);
    white-space: nowrap;
  }
  .tagline {
    position: absolute;
    left: 60px;
    top: 168px;
    margin: 0;
    font-size: 22px;
    font-weight: 400;
    line-height: 1;
    letter-spacing: 0.18em;
    color: var(--tagline-grey);
    white-space: nowrap;
  }
  .blossom-photo {
    position: absolute;
    left: 800px;
    top: 25px;
    width: 400px;
    height: 205px;
    background: radial-gradient(ellipse 60% 55% at 60% 45%, var(--blossom-mid), var(--blossom-light) 55%, var(--paper) 100%);
  }
</style>
</head>
<body>
  <header class="banner">
    <h1 class="brand-name">Bright Marrow</h1>
    <p class="tagline">Steady Sparks for crowded calendars</p>
    <div class="blossom-photo" role="img" aria-label="Photograph of a branch with pale peach cherry blossoms on white"></div>
  </header>
</body>
</html>
```